Business Card Design

A new interior design company specialising in residential property styling, with a focus on styling properties for sale. We aim to present the property to increase marketability, saleability and hopefully get the best price.
We are looking for a design that stands out from the crowd maybe using colour and maybe pattern, something that is modern and fits in with companies aesthetic of design.
We would like the design not to be too fussy, with perhaps all of the contact information on the back (ie just the company name on front?)

Industry/Entity Type

Residential

Contact Information for Business Card

Velvane Interiors, Clara Dunstow, Interior Designer,0412736509, velvaneinteriors@mailbox-example.com.au

Requirements
Nice to have
• Velvane means "love" in Spanish and I was wondering whether it might be too corny to use the M in vElvane that resembles a love heart, something curvy. This is just an idea I've was toying with and I am completely open to other suggestions.

```html
<!DOCTYPE html>
<html lang="en">
<head>
<meta charset="utf-8">
<title>Velvane Interiors — Business Card</title>
<link rel="stylesheet" href="https://fonts.googleapis.com/css2?family=Open+Sans:wght@300;400&display=swap">
<style>
  :root {
    --backdrop: #1f2022;
    --card-front: #d6c79c;
    --card-back: #ec836a;
    --ink-light: #ffffff;
    --ink-soft: rgba(255, 255, 255, 0.88);
  }
  html, body {
    margin: 0;
    padding: 0;
    width: 1200px;
    height: 1000px;
    overflow: hidden;
    background: var(--backdrop);
    font-family: "Open Sans", Arial, sans-serif;
  }
  .stage {
    position: relative;
    width: 1200px;
    height: 1000px;
  }
  .card {
    position: absolute;
    width: 520px;
    height: 300px;
    border-radius: 12px;
    box-sizing: border-box;
    color: var(--ink-light);
  }
  .card--front {
    left: 90px;
    top: 540px;
    background: var(--card-front);
    display: flex;
    align-items: center;
    justify-content: center;
  }
  .brand-name {
    font-weight: 400;
    font-size: 40px;
    letter-spacing: 0.5px;
    color: var(--ink-light);
    margin: 0;
  }
  .card--back {
    left: 590px;
    top: 170px;
    background: var(--card-back);
  }
  .holder {
    position: absolute;
    left: 26px;
    top: 22px;
    margin: 0;
  }
  .holder-name {
    display: block;
    font-weight: 400;
    font-size: 17px;
    line-height: 22px;
  }
  .holder-role {
    display: block;
    font-weight: 300;
    font-size: 16px;
    line-height: 20px;
    color: var(--ink-soft);
  }
  .measure-line {
    position: absolute;
    left: 0;
    top: 0;
    width: 520px;
    height: 300px;
  }
  .contact-list {
    position: absolute;
    left: 290px;
    top: 222px;
    margin: 0;
    padding: 0;
    list-style: none;
    font-weight: 300;
    font-size: 13px;
    line-height: 22px;
  }
  .contact-item {
    display: flex;
    align-items: center;
    gap: 8px;
  }
  .contact-icon {
    width: 12px;
    height: 12px;
    flex: none;
  }
</style>
</head>
<body>
<main class="stage">
  <section class="card card--front" aria-label="Business card front">
    <h1 class="brand-name">Velvane Interiors</h1>
  </section>

  <section class="card card--back" aria-label="Business card back">
    <p class="holder">
      <span class="holder-name">Clara Dunstow</span>
      <span class="holder-role">Interior Designer</span>
    </p>

    <svg class="measure-line" viewBox="0 0 520 300" aria-hidden="true">
      <g stroke="#ffffff" stroke-width="1" fill="none">
        <line x1="160" y1="66" x2="330" y2="66"/>
        <line x1="300" y1="72" x2="300" y2="206"/>
        <line x1="272" y1="212" x2="320" y2="212"/>
      </g>
      <g fill="#ffffff">
        <polygon points="300,68 296,78 304,78"/>
        <polygon points="300,210 296,200 304,200"/>
      </g>
    </svg>

    <ul class="contact-list">
      <li class="contact-item">
        <svg class="contact-icon" viewBox="0 0 12 12" aria-hidden="true">
          <rect x="3" y="0.5" width="6" height="11" rx="1" fill="none" stroke="#ffffff" stroke-width="1"/>
          <rect x="4.2" y="2" width="3.6" height="5" fill="#ffffff"/>
        </svg>
        <span>0412 736 509</span>
      </li>
      <li class="contact-item">
        <svg class="contact-icon" viewBox="0 0 12 12" aria-hidden="true">
          <rect x="0.5" y="2.5" width="11" height="7" fill="#ffffff"/>
          <polyline points="0.5,2.5 6,7 11.5,2.5" fill="none" stroke="#ec836a" stroke-width="1"/>
        </svg>
        <span>velvaneinteriors@mailbox-example.com.au</span>
      </li>
    </ul>
  </section>
</main>
</body>
</html>
```